Textbook cover for dental seminar

I'm looking for a fresh new design for our annual textbook. You will need to incorporate our logo, business name (BeccaCDT's Dental Hygiene Institute) - the words "BeccaCDT's" needs to be larger or the same size as "Dental Hygiene Academy" and colors of dentistry is purple so I like to stick with shades of purple in the design however it does not need to be all purple or only purple. The words "with hygiene career booster" will not be on next years edition so please do not add that. The book will have spiral binding so please account for that when designing. Please see our website for information BeccaCDTExamPrep.example
Updates

I also want listed on the cover somewhere “The World’s First Interactive Review Book!”

Size will be 8.5" x 11"

```html
<!DOCTYPE html>
<html lang="en">
<head>
<meta charset="utf-8">
<title>BeccaCDT's Dental Hygiene Institute – Dental Hygiene Board Review 2022</title>
<link rel="stylesheet" href="https://fonts.googleapis.com/css2?family=Roboto+Condensed:wght@300;400;700&display=swap">
<style>
  :root {
    --page-bg: #6a5a86;
    --cover-deep: #2a1a6e;
    --cover-mid: #4b2a9a;
    --cover-bright: #8a4fd0;
    --ribbon: #b9b2d9;
    --ribbon-text: #3a2b7a;
    --title-white: #f4f2fa;
    --tagline: #e2d6f7;
    --badge-ring: #5b2f9a;
  }
  * { margin: 0; padding: 0; box-sizing: border-box; }
  html, body {
    width: 1200px;
    height: 1200px;
    overflow: hidden;
  }
  body {
    background: var(--page-bg);
    font-family: "Roboto Condensed", sans-serif;
    position: relative;
  }
  .cover {
    position: absolute;
    left: 195px;
    top: 70px;
    width: 810px;
    height: 1060px;
    overflow: hidden;
    background:
      radial-gradient(ellipse 70% 22% at 40% 50%, rgba(170, 110, 230, 0.55), transparent 70%),
      radial-gradient(ellipse 55% 35% at 20% 28%, rgba(140, 80, 210, 0.45), transparent 70%),
      linear-gradient(160deg, var(--cover-deep) 0%, var(--cover-mid) 45%, var(--cover-bright) 58%, var(--cover-mid) 72%, var(--cover-deep) 100%);
  }
  .cover-art {
    position: absolute;
    inset: 0;
    width: 100%;
    height: 100%;
  }
  .brand-mark {
    position: absolute;
    left: 97px;
    top: 170px;
    display: flex;
    align-items: center;
    gap: 22px;
  }
  .brand-mark__dot {
    width: 120px;
    height: 120px;
    border-radius: 50%;
    background: var(--badge-ring);
    flex: none;
  }
  .brand-mark__name {
    color: var(--title-white);
    font-weight: 700;
    font-size: 30px;
    line-height: 1.15;
    text-transform: uppercase;
    max-width: 300px;
  }
  .title {
    position: absolute;
    left: 97px;
    top: 430px;
    color: var(--title-white);
    font-weight: 700;
    text-transform: uppercase;
    font-size: 100px;
    line-height: 1;
  }
  .title__owner {
    display: block;
    font-size: 100px;
    line-height: 1;
  }
  .title__institute {
    display: block;
    margin-top: 11px;
    font-size: 73px;
    line-height: 83px;
  }
  .tagline {
    position: absolute;
    left: 97px;
    top: 738px;
    color: var(--tagline);
    font-weight: 400;
    font-size: 30px;
    line-height: 1;
  }
  .subtitle {
    position: absolute;
    left: 97px;
    top: 820px;
    color: var(--title-white);
    font-weight: 300;
    font-size: 64px;
    line-height: 77px;
    text-transform: uppercase;
  }
  .edition-year {
    position: absolute;
    right: 62px;
    bottom: 16px;
    color: var(--title-white);
    font-weight: 700;
    font-size: 72px;
    line-height: 1;
  }
  .web-ribbon {
    position: absolute;
    top: 0;
    right: 0;
    width: 96px;
    height: 911px;
    background: var(--ribbon);
    opacity: 0.9;
    clip-path: polygon(0 0, 100% 0, 100% 100%, 0 93.5%);
  }
  .web-ribbon__address {
    position: absolute;
    left: 50%;
    top: 77px;
    transform: translateX(-50%);
    writing-mode: vertical-rl;
    color: var(--ribbon-text);
    font-weight: 700;
    font-size: 42px;
    line-height: 1;
    letter-spacing: 1px;
    text-transform: uppercase;
    white-space: nowrap;
  }
</style>
</head>
<body>
  <main class="cover">
    <svg class="cover-art" viewBox="0 0 810 1060" role="img" aria-label="Abstract purple light streaks across a starry background" preserveAspectRatio="none">
      <defs>
        <linearGradient id="streak" x1="0" y1="0" x2="1" y2="0">
          <stop offset="0" stop-color="#c79cf2" stop-opacity="0"/>
          <stop offset="0.5" stop-color="#c79cf2" stop-opacity="0.35"/>
          <stop offset="1" stop-color="#c79cf2" stop-opacity="0"/>
        </linearGradient>
      </defs>
      <path d="M0 620 C 250 560, 500 430, 810 330 L 810 380 C 520 470, 260 600, 0 680 Z" fill="url(#streak)"/>
      <path d="M0 520 C 300 500, 560 420, 810 420 L 810 450 C 560 460, 300 540, 0 560 Z" fill="url(#streak)"/>
    </svg>

    <div class="brand-mark">
      <span class="brand-mark__dot"></span>
      <span class="brand-mark__name">BeccaCDT's Dental Hygiene Institute</span>
    </div>

    <h1 class="title">
      <span class="title__owner">BeccaCDT's</span>
      <span class="title__institute">Dental Hygiene<br>Institute</span>
    </h1>

    <p class="tagline">The World's First Interactive Review Book!</p>

    <p class="subtitle">Dental Hygiene<br>Board Review</p>

    <p class="edition-year">2022</p>

    <aside class="web-ribbon">
      <span class="web-ribbon__address">www.BeccaCDTExamPrep.example</span>
    </aside>
  </main>
</body>
</html>
```